Business Card and stationery
Use same font as used in my logo
Delia Frost
4127 E Copper Ln
Fernvale, Or 85299
delia@thewillowparlorshop.com
www.thewillowparlorshop.com
Store Hours
Tue & Thu 10am - 4 pm
And By Appointment

```html
<!DOCTYPE html>
<html lang="en">
<head>
<meta charset="utf-8">
<title>Larkspur Stationery Set</title>
<link rel="stylesheet" href="https://fonts.googleapis.com/css2?family=Lato:wght@400;700&display=swap">
<style>
  :root {
    --magenta: #d4137f;
    --ink: #1a1a1a;
    --muted: #6b6b6b;
    --paper: #ffffff;
    --rule: #c9c9c9;
    --stage: #ffffff;
    --faint: #ececef;
  }
  * { box-sizing: border-box; margin: 0; padding: 0; }
  html, body { width: 1200px; height: 482px; overflow: hidden; background: var(--stage); }
  body { position: relative; font-family: "Lato", Arial, sans-serif; color: var(--ink); }

  .sheet, .envelope, .card {
    position: absolute; background: var(--paper);
    box-shadow: 0 1px 4px rgba(0,0,0,.18);
  }
  .band { position: absolute; left: 0; right: 0; background: var(--magenta); }
  .brand {
    position: absolute; background: var(--paper);
    display: flex; align-items: center; gap: 4px;
  }
  .brand-mark { width: 8px; height: 8px; background: var(--ink); flex: none; }
  .brand-name { font-weight: 700; color: var(--ink); letter-spacing: .3px; white-space: nowrap; }

  .contact { position: absolute; font-size: 5px; line-height: 7px; color: var(--muted); white-space: nowrap; }
  .faint-mark {
    position: absolute; border-radius: 50%;
    background: radial-gradient(circle, var(--faint), rgba(236,236,239,0) 70%);
  }

  /* fax sheet */
  .fax { left: 19px; top: 24px; width: 346px; height: 414px; }
  .fax .band { top: 10px; height: 26px; }
  .fax .brand { left: 10px; top: 6px; height: 34px; padding: 0 8px; }
  .fax .brand-name { font-size: 15px; }
  .fax .contact { left: 16px; top: 48px; }
  .fax-fields {
    position: absolute; left: 16px; top: 128px; width: 300px;
    display: grid; grid-template-columns: 1fr 1fr; gap: 14px 20px;
    font-size: 6px; color: var(--muted);
  }
  .field { display: flex; align-items: flex-end; gap: 6px; }
  .field span { width: 26px; }
  .field i { flex: 1; border-bottom: 1px solid var(--rule); }
  .fax-checks {
    position: absolute; left: 16px; top: 214px; display: flex; gap: 16px;
    font-size: 5.5px; color: var(--muted);
  }
  .fax-checks label { display: flex; align-items: center; gap: 3px; }
  .fax-checks label::before {
    content: ""; width: 6px; height: 6px; border: 1px solid var(--muted); border-radius: 50%;
  }
  .fax .faint-mark { left: 200px; top: 250px; width: 130px; height: 150px; }

  /* envelopes */
  .env-front { left: 396px; top: 77px; width: 350px; height: 156px; }
  .env-front .band { top: 10px; height: 26px; }
  .env-front .brand { left: 10px; top: 6px; height: 34px; padding: 0 8px; }
  .env-front .brand-name { font-size: 15px; }
  .env-front .contact { left: 14px; top: 46px; }
  .env-back { left: 396px; top: 257px; width: 350px; height: 156px; }
  .env-back svg { position: absolute; inset: 0; }
  .env-back .brand { left: 150px; top: 36px; padding: 2px; }
  .env-back .brand-mark { width: 6px; height: 6px; }
  .env-back .brand-name { font-size: 7px; }

  /* letterhead */
  .letterhead { left: 794px; top: 24px; width: 324px; height: 414px; }
  .letterhead .band { top: 10px; height: 26px; }
  .letterhead .brand { left: 10px; top: 6px; height: 34px; padding: 0 8px; }
  .letterhead .brand-name { font-size: 15px; }
  .letterhead .contact { left: 16px; top: 48px; }
  .letterhead .faint-mark { left: 150px; top: 250px; width: 130px; height: 150px; }

  /* business cards */
  .card-front { left: 1034px; top: 108px; width: 88px; height: 50px; }
  .card-front .band { top: 0; height: 14px; }
  .card-front .brand { left: 4px; top: 3px; padding: 1px 3px; }
  .card-front .brand-mark { width: 4px; height: 4px; }
  .card-front .brand-name { font-size: 7px; }
  .card-front .contact { left: 5px; top: 19px; font-size: 3px; line-height: 4.6px; }
  .card-back { left: 1034px; top: 190px; width: 140px; height: 76px; background: var(--magenta); }
  .card-back .brand { left: 0; right: 0; top: 28px; justify-content: center; background: transparent; }
  .card-back .brand-mark { width: 6px; height: 6px; background: var(--paper); }
  .card-back .brand-name { font-size: 12px; color: var(--paper); }

  .baseline { position: absolute; left: 0; right: 0; top: 456px; height: 1px; background: var(--rule); }
</style>
</head>
<body>

  <section class="sheet fax" aria-label="Fax cover sheet">
    <div class="band"></div>
    <div class="brand"><span class="brand-mark"></span><span class="brand-name">Larkspur</span></div>
    <p class="contact">4127 E Copper Ln<br>Fernvale, Or 85299<br>T 541.555.0142<br>F 541.555.0143<br>delia@thewillowparlorshop.com<br>www.thewillowparlorshop.com</p>
    <div class="fax-fields">
      <div class="field"><span>To:</span><i></i></div>
      <div class="field"><span>From:</span><i></i></div>
      <div class="field"><span>Fax:</span><i></i></div>
      <div class="field"><span>Pages:</span><i></i></div>
      <div class="field"><span>Phone:</span><i></i></div>
      <div class="field"><span>Date:</span><i></i></div>
      <div class="field"><span>Re:</span><i></i></div>
      <div class="field"><span>CC:</span><i></i></div>
    </div>
    <div class="fax-checks">
      <label>Urgent</label><label>For Review</label><label>Please Comment</label><label>Please Reply</label><label>Please Recycle</label>
    </div>
    <div class="faint-mark" role="img" aria-label="Faint brand decoration"></div>
  </section>

  <section class="envelope env-front" aria-label="Envelope front">
    <div class="band"></div>
    <div class="brand"><span class="brand-mark"></span><span class="brand-name">Larkspur</span></div>
    <p class="contact">4127 E Copper Ln &middot; Fernvale, Or 85299</p>
  </section>

  <section class="envelope env-back" aria-label="Envelope back">
    <svg viewBox="0 0 350 156" width="350" height="156" aria-hidden="true">
      <polyline points="0,0 175,60 350,0" fill="none" stroke="#c9c9c9" stroke-width="1"/>
    </svg>
    <div class="brand"><span class="brand-mark"></span><span class="brand-name">Larkspur</span></div>
  </section>

  <section class="sheet letterhead" aria-label="Letterhead">
    <div class="band"></div>
    <div class="brand"><span class="brand-mark"></span><span class="brand-name">Larkspur</span></div>
    <p class="contact">4127 E Copper Ln<br>Fernvale, Or 85299<br>T 541.555.0142<br>F 541.555.0143<br>delia@thewillowparlorshop.com<br>www.thewillowparlorshop.com</p>
    <div class="faint-mark" role="img" aria-label="Faint brand decoration"></div>
  </section>

  <section class="card card-front" aria-label="Business card front">
    <div class="band"></div>
    <div class="brand"><span class="brand-mark"></span><span class="brand-name">Larkspur</span></div>
    <p class="contact">Delia Frost<br>4127 E Copper Ln, Fernvale, Or 85299<br>delia@thewillowparlorshop.com<br>Tue &amp; Thu 10am - 4 pm &middot; By Appointment</p>
  </section>

  <section class="card card-back" aria-label="Business card back">
    <div class="brand"><span class="brand-mark"></span><span class="brand-name">Larkspur</span></div>
  </section>

  <div class="baseline"></div>
</body>
</html>
```